Webdesign für IT-Dienstleister
Zielgruppe
Seit 1997 bieten wir erstklassige IT-Dienstleistungen Mainz an, die darauf ausgerichtet sind, Unternehmen und Privatkunden mit kompetenter Beratung, zuverlässiger Unterstützung und modernen Technologielösungen zur Seite zu stehen.
Umfassende Computer-Serviceleistungen
Unser Computer-Service Mainz beinhaltet eine Reihe von Dienstleistungen, die darauf abzielen, die Leistungsfähigkeit Ihrer IT-Infrastruktur zu optimieren und zu erhalten. Von der Fehlerdiagnose bis hin zur Wartung bieten wir ein Rundum-Sorglos-Paket für Ihre Hardware und Software.
Professionelle Fehleranalyse und Reparatur
Optimierung von Betriebssystemen und Anwendungen
Regelmäßige Wartungsarbeiten zur Vorbeugung von Ausfällen
Ersetzen und Aufrüsten von Hardware-Komponenten
Aufgabenstellung
Ich hätte gern ein modernes Design. Ein Logo vorhanden, sollte mit eingebaut werden.
Ansonsten hätte ich gerne eine einzelne Webseite mit den Firmen Infos (und den Links zu Sozial Media) und einer extra Impressum Seite. Und wenn möglich noch ein Anfrage Formular.
Am liebsten wäre ein Format welches ich in WordPress verarbeiten werden kann.
(Logo wird noch nachgereicht)

```html
<!DOCTYPE html>
<html lang="de">
<head>
<meta charset="utf-8">
<title>pcwerk-rhein.de – IT-Dienstleistungen in Mainz</title>
<link rel="stylesheet" href="https://fonts.googleapis.com/css2?family=Poppins:wght@400;500;600;700;800&display=swap">
<style>
:root{
  --primary:#29b0dc;
  --primary-soft:#e6f6fc;
  --navy:#1b2a4a;
  --text:#2b3447;
  --muted:#5d6678;
  --line:#e6e9ef;
  --section:#f7f8fa;
  --footer:#141b2d;
  --white:#fff;
}
*{box-sizing:border-box;margin:0;padding:0}
html,body{width:1200px;height:3149px;overflow:hidden}
body{font-family:"Poppins",sans-serif;color:var(--text);background:var(--white)}
.container{width:1050px;margin:0 auto;position:relative}
svg.ic{width:16px;height:16px;fill:none;stroke:var(--primary);stroke-width:1.8;stroke-linecap:round;stroke-linejoin:round}

/* top bar */
.topbar{height:30px;background:var(--primary);color:#fff;font-size:12px}
.topbar .container{display:flex;align-items:center;height:30px;gap:24px}
.topbar span{display:flex;align-items:center;gap:6px}
.topbar svg{stroke:#fff;width:11px;height:11px}
.topbar .social{margin-left:auto;display:flex;gap:16px}
.topbar .social i{width:10px;height:10px;border:1.5px solid #fff;border-radius:50%;display:block}

/* nav */
.nav{height:55px;border-bottom:1px solid var(--line);background:#fff}
.nav .container{display:flex;align-items:center;height:55px}
.brand{display:flex;align-items:center;gap:8px;font-weight:600;font-size:20px;color:var(--navy)}
.brand i{width:30px;height:30px;border-radius:50%;border:3px solid var(--primary);display:block}
.nav ul{margin-left:auto;display:flex;gap:27px;list-style:none;font-size:14px;font-weight:500;color:var(--navy)}

/* hero */
.hero{height:501px;background:linear-gradient(180deg,#e3f5fc 0%,#f6fbfe 70%,#fff 100%)}
.hero h1{position:absolute;top:62px;left:0;width:560px;font-size:43px;line-height:1;font-weight:700;color:var(--navy)}
.hero p.lead{position:absolute;top:163px;left:0;width:490px;font-size:17px;line-height:1.4;color:var(--text)}
.btn{display:inline-block;background:var(--primary);color:#fff;font-weight:600;font-size:15px;border-radius:5px}
.hero .btn{position:absolute;top:307px;left:0;width:288px;height:51px;line-height:51px;text-align:center}
.hero-media{position:absolute;top:135px;left:525px;width:525px;height:183px;border-radius:50%/40%;background:radial-gradient(ellipse at center,#c9d3de 0%,#e9eef3 55%,rgba(255,255,255,0) 75%)}
.features{position:absolute;top:392px;left:-14px;display:flex;gap:20px}
.feature{display:flex;gap:12px;align-items:center}
.feature .badge{width:40px;height:40px;border-radius:10px;background:var(--primary-soft);display:flex;align-items:center;justify-content:center}
.feature b{display:block;font-size:13px;font-weight:600;color:var(--navy)}
.feature small{font-size:12px;color:var(--muted)}

/* services */
.services{height:842px;background:var(--section);padding-top:66px}
.section-title{text-align:center;font-size:31px;font-weight:700;color:var(--navy)}
.section-sub{text-align:center;font-size:17px;color:var(--muted);margin-top:10px}
.grid{display:grid;grid-template-columns:repeat(3,332px);gap:27px 27px;margin-top:55px}
.card{height:277px;background:#fff;border:1px solid var(--line);border-radius:10px;overflow:hidden;position:relative}
.card .media{height:134px}
.card .pin{position:absolute;top:114px;left:142px;width:46px;height:46px;border-radius:50%;background:#fff;box-shadow:0 2px 8px rgba(0,0,0,.12);display:flex;align-items:center;justify-content:center}
.card h3{margin:36px 20px 0;font-size:18px;font-weight:600;line-height:1.35;color:var(--navy)}
.card p{margin:6px 20px 0;font-size:12px;line-height:1.45;color:var(--muted)}
.card p em{font-style:normal;color:var(--primary)}
.m1{background:linear-gradient(135deg,#d9dde2,#9ea6ae 60%,#3a3f46)}
.m2{background:linear-gradient(135deg,#b9c0c8,#e4e8ec 55%,#8a939c)}
.m3{background:linear-gradient(135deg,#57606a,#1f2a33 60%,#7a8590)}
.m4{background:linear-gradient(135deg,#0d1c33,#1e4f8c 50%,#0b1626)}
.m5{background:linear-gradient(135deg,#aab4bf,#3c4550 55%,#c3ccd6)}
.m6{background:linear-gradient(135deg,#dfe7ee,#a9c9e6 55%,#e9eff4)}

/* about */
.about{height:478px;padding-top:0}
.about h2{position:absolute;top:84px;left:0;width:520px;font-size:31px;line-height:1.12;font-weight:700;color:var(--navy)}
.about p{position:absolute;top:156px;left:0;width:500px;font-size:15px;line-height:1.6;color:var(--text)}
.checks{position:absolute;top:277px;left:0;width:520px;display:grid;grid-template-columns:266px 240px;row-gap:24px}
.check{display:flex;gap:10px}
.check b{display:block;font-size:13px;font-weight:600;color:var(--navy)}
.check small{display:block;font-size:12px;line-height:1.45;color:var(--muted)}
.about-media{position:absolute;top:79px;left:545px;width:505px;height:322px;border-radius:10px;background:linear-gradient(180deg,#d5dbe2 0%,#eef1f4 40%,#b6a79a 100%);box-shadow:0 8px 20px rgba(0,0,0,.12)}

/* contact */
.contact{height:859px;background:var(--section);padding-top:64px}
.info{position:absolute;top:208px;left:0;width:420px}
.info h3{font-size:20px;font-weight:600;color:var(--navy);margin-bottom:27px}
.info-item{display:flex;gap:14px;margin-bottom:22px}
.info-item .badge{width:40px;height:40px;border-radius:50%;background:var(--primary-soft);display:flex;align-items:center;justify-content:center;flex:none}
.info-item b{display:block;font-size:14px;font-weight:600;color:var(--navy);margin-bottom:4px}
.info-item span{display:block;font-size:14px;line-height:1.45;color:var(--text)}
.form{position:absolute;top:194px;left:545px;width:505px;height:597px;background:#fff;border-radius:12px;padding:26px 26px}
.form h3{font-size:20px;font-weight:600;color:var(--navy);margin-bottom:21px}
.row{display:flex;gap:14px}
.field{flex:1;margin-bottom:19px}
.field label{display:block;font-size:12px;font-weight:500;margin-bottom:8px;color:var(--text)}
.field .input{height:39px;border:1px solid #d4d8e0;border-radius:7px}
.field .area{height:106px}
.consent{display:flex;gap:10px;font-size:12px;line-height:1.45;margin-top:6px}
.consent i{width:14px;height:14px;border:1px solid #9aa1ad;border-radius:2px;flex:none;margin-top:2px}
.form .btn{display:block;width:452px;height:40px;line-height:40px;text-align:center;font-size:14px;margin-top:22px;border-radius:4px}

/* footer */
.footer{height:384px;background:var(--footer);color:#c7ccd6}
.footer .cols{display:grid;grid-template-columns:360px 360px 330px;padding-top:60px}
.footer .brand{color:#fff;font-size:20px}
.footer p{font-size:13px;line-height:1.55;margin-top:18px;width:300px}
.footer .social{display:flex;gap:14px;margin-top:16px}
.footer .social i{width:26px;height:26px;border-radius:50%;background:#222b3f;display:block}
.footer h4{color:#fff;font-size:15px;font-weight:600;margin-top:15px;margin-bottom:16px}
.footer .fi{display:flex;gap:14px;font-size:14px;line-height:1.45;margin-bottom:12px}
.footer .fi svg{width:11px;height:11px;stroke:#7c8596;margin-top:5px;flex:none}
.footer ul{list-style:none;font-size:14px}
.footer li{margin-bottom:12px}
.copy{position:absolute;top:304px;left:0;width:1050px;border-top:1px solid #263047;padding-top:30px;text-align:center;font-size:13px}
</style>
</head>
<body>
<svg width="0" height="0" style="position:absolute">
  <defs>
    <symbol id="i-phone" viewBox="0 0 24 24"><path d="M22 16.9v3a2 2 0 0 1-2.2 2A19.8 19.8 0 0 1 2.1 4.2 2 2 0 0 1 4.1 2h3a2 2 0 0 1 2 1.7l.5 3a2 2 0 0 1-.6 1.8L7.6 9.8a16 16 0 0 0 6.6 6.6l1.3-1.3a2 2 0 0 1 1.8-.6l3 .5a2 2 0 0 1 1.7 2z"/></symbol>
    <symbol id="i-mail" viewBox="0 0 24 24"><rect x="3" y="5" width="18" height="14" rx="2"/><path d="m3 7 9 6 9-6"/></symbol>
    <symbol id="i-pin" viewBox="0 0 24 24"><path d="M12 22s7-6.3 7-12a7 7 0 0 0-14 0c0 5.7 7 12 7 12z"/><circle cx="12" cy="10" r="2.5"/></symbol>
    <symbol id="i-clock" viewBox="0 0 24 24"><circle cx="12" cy="12" r="9"/><path d="M12 7v5l3 2"/></symbol>
    <symbol id="i-bolt" viewBox="0 0 24 24"><path d="M13 2 4 14h7l-1 8 9-12h-7z"/></symbol>
    <symbol id="i-user" viewBox="0 0 24 24"><circle cx="11" cy="8" r="4"/><path d="M4 21a7 7 0 0 1 11-5.7M17 17l2 2 3-3"/></symbol>
    <symbol id="i-tools" viewBox="0 0 24 24"><path d="M4 4l16 16M20 4 4 20M4 4h4M20 4v4"/></symbol>
    <symbol id="i-code" viewBox="0 0 24 24"><rect x="3" y="4" width="18" height="16" rx="2"/><path d="m9 10-2 2 2 2M15 10l2 2-2 2M13 9l-2 6"/></symbol>
    <symbol id="i-bag" viewBox="0 0 24 24"><rect x="4" y="6" width="16" height="15" rx="2"/><path d="M9 10a3 3 0 0 0 6 0M9 6V4h6v2"/></symbol>
    <symbol id="i-net" viewBox="0 0 24 24"><rect x="4" y="13" width="16" height="7" rx="2"/><path d="M8 9a6 6 0 0 1 8 0M5 6a10 10 0 0 1 14 0"/></symbol>
    <symbol id="i-shield" viewBox="0 0 24 24"><path d="M12 3 4 6v6c0 5 3.5 8 8 9 4.5-1 8-4 8-9V6z"/><path d="m9 12 2 2 4-4"/></symbol>
    <symbol id="i-wifi" viewBox="0 0 24 24"><path d="M2 9a15 15 0 0 1 20 0M5 13a10 10 0 0 1 14 0M8.5 16.5a5 5 0 0 1 7 0"/><circle cx="12" cy="20" r=".8"/></symbol>
    <symbol id="i-tick" viewBox="0 0 24 24"><path d="m5 12 5 5 9-10"/></symbol>
  </defs>
</svg>

<header>
  <div class="topbar">
    <div class="container">
      <span><svg class="ic"><use href="#i-phone"/></svg>+49 6131 554870</span>
      <span><svg class="ic"><use href="#i-mail"/></svg>info@pcwerk-rhein.de</span>
      <div class="social" aria-label="Soziale Netzwerke"><i></i><i></i><i></i></div>
    </div>
  </div>
  <nav class="nav">
    <div class="container">
      <div class="brand"><i></i>pcwerk-rhein.de</div>
      <ul><li>Home</li><li>Services</li><li>Kontakt</li><li>Impressum</li></ul>
    </div>
  </nav>
</header>

<section class="hero">
  <div class="container">
    <h1>Ihr IT-Partner in Mainz &amp; Umgebung</h1>
    <p class="lead">Verlassen Sie sich auf zuverlässige IT-Lösungen und persönlichen Service – für Unternehmen &amp; Privatkunden. Wir bieten schnelle Hilfe, persönliche Beratung und maßgeschneiderte Lösungen rund um Computer, Netzwerke und mehr.</p>
    <a class="btn">Jetzt kostenlos beraten lassen</a>
    <div class="hero-media" role="img" aria-label="Computer, Monitore, Drucker, Laptop und Zubehör auf einer runden Fläche"></div>
    <div class="features">
      <div class="feature"><div class="badge"><svg class="ic"><use href="#i-bolt"/></svg></div><div><b>Schnelle Hilfe</b><small>Vor-Ort &amp; Fernwartung</small></div></div>
      <div class="feature"><div class="badge"><svg class="ic"><use href="#i-user"/></svg></div><div><b>Persönliche Beratung</b><small>Individuell &amp; ehrlich</small></div></div>
      <div class="feature"><div class="badge"><svg class="ic"><use href="#i-tools"/></svg></div><div><b>Maßgeschneiderte Lösungen</b><small>Für jede Anforderung</small></div></div>
    </div>
  </div>
</section>

<section class="services">
  <div class="container">
    <h2 class="section-title">Unsere Services</h2>
    <p class="section-sub">Umfassende Computer-Serviceleistungen für optimale IT-Performance</p>
    <div class="grid">
      <article class="card"><div class="media m1" role="img" aria-label="Laptop mit Programmcode auf einem Schreibtisch"></div><div class="pin"><svg class="ic"><use href="#i-code"/></svg></div><h3>Softwareentwicklung &amp; Anpassungen</h3><p>Wir entwickeln <em>maßgeschneiderte Software</em> und <em>individuelle Programme</em> für Ihren Erfolg.</p></article>
      <article class="card"><div class="media m2" role="img" aria-label="Tastatur, Maus und Headset"></div><div class="pin"><svg class="ic"><use href="#i-bag"/></svg></div><h3>Computerzubehör &amp; Beratung</h3><p><em>Umfangreiches Sortiment</em> und persönliche Beratung in unserem Mainzer Shop.</p></article>
      <article class="card"><div class="media m3" role="img" aria-label="Reparatur an einer Hauptplatine neben einer Festplatte"></div><div class="pin"><svg class="ic"><use href="#i-tools"/></svg></div><h3>Fehlerdiagnose &amp; Reparatur</h3><p>Professionelle <em>Analyse</em> und <em>Reparatur</em> Ihrer Geräte – schnell, zuverlässig und transparent.</p></article>
      <article class="card"><div class="media m4" role="img" aria-label="Serverschrank mit blauen Netzwerkkabeln"></div><div class="pin"><svg class="ic"><use href="#i-net"/></svg></div><h3>Computernetzwerk-Dienstleistungen</h3><p>Effiziente <em>Vernetzung</em> und <em>IT-Infrastruktur</em> für Unternehmen.</p></article>
      <article class="card"><div class="media m5" role="img" aria-label="Geöffneter Laptop bei der Wartung"></div><div class="pin"><svg class="ic"><use href="#i-shield"/></svg></div><h3>Service &amp; Wartungsverträge</h3><p>Individuelle <em>Wartungspakete</em> für eine sorgenfreie IT.</p></article>
      <article class="card"><div class="media m6" role="img" aria-label="Router mit leuchtendem WLAN-Symbol"></div><div class="pin"><svg class="ic"><use href="#i-wifi"/></svg></div><h3>DSL &amp; Internet Produkte</h3><p>Passende <em>Internetlösungen</em> für Privat- und Geschäftskunden.</p></article>
    </div>
  </div>
</section>

<section class="about">
  <div class="container">
    <h2>Über 25 Jahre Erfahrung in der IT-Branche</h2>
    <p>Seit 1997 sind wir Ihr vertrauensvoller Partner für alle IT-Angelegenheiten in Mainz. Mit unserem erfahrenen Team und modernster Ausstattung lösen wir auch komplexeste technische Herausforderungen zuverlässig und effizient.</p>
    <div class="checks">
      <div class="check"><svg class="ic"><use href="#i-tick"/></svg><div><b>Zertifizierte Experten</b><small>Kontinuierliche Weiterbildung unseres Teams</small></div></div>
      <div class="check"><svg class="ic"><use href="#i-tick"/></svg><div><b>24/7 Support</b><small>Notfall-Service für kritische Systeme</small></div></div>
      <div class="check"><svg class="ic"><use href="#i-tick"/></svg><div><b>Faire Preise</b><small>Transparente Kostenstruktur ohne versteckte Gebühren</small></div></div>
      <div class="check"><svg class="ic"><use href="#i-tick"/></svg><div><b>Vor-Ort-Service</b><small>Schnelle Hilfe direkt bei Ihnen vor Ort</small></div></div>
    </div>
    <div class="about-media" role="img" aria-label="Helles Großraumbüro mit Arbeitsplätzen und Monitoren"></div>
  </div>
</section>

<section class="contact">
  <div class="container">
    <h2 class="section-title">Kontakt aufnehmen</h2>
    <p class="section-sub">Haben Sie Fragen oder benötigen Sie Unterstützung? Wir sind für Sie da!</p>
    <div class="info">
      <h3>Kontaktinformationen</h3>
      <div class="info-item"><div class="badge"><svg class="ic"><use href="#i-pin"/></svg></div><div><b>Adresse</b><span>Lindenweg 14<br>55116 Mainz<br>Deutschland</span></div></div>
      <div class="info-item"><div class="badge"><svg class="ic"><use href="#i-phone"/></svg></div><div><b>Telefon</b><span>+49 6131 554870<br>Fax: +49 6131 554871</span></div></div>
      <div class="info-item"><div class="badge"><svg class="ic"><use href="#i-mail"/></svg></div><div><b>E-Mail</b><span>info@pcwerk-rhein.de<br>support@pcwerk-rhein.de</span></div></div>
      <div class="info-item"><div class="badge"><svg class="ic"><use href="#i-clock"/></svg></div><div><b>Öffnungszeiten</b><span>Mo–Fr: 08:00 - 18:00 Uhr<br>Sa: 09:00 - 14:00 Uhr<br>So: Geschlossen</span></div></div>
    </div>
    <form class="form">
      <h3>Anfrage senden</h3>
      <div class="row">
        <div class="field"><label>Name *</label><div class="input"></div></div>
        <div class="field"><label>E-Mail *</label><div class="input"></div></div>
      </div>
      <div class="field"><label>Telefon</label><div class="input"></div></div>
      <div class="field"><label>Betreff *</label><div class="input"></div></div>
      <div class="field"><label>Nachricht *</label><div class="input area"></div></div>
      <div class="consent"><i></i><span>Ich stimme der Verarbeitung meiner Daten gemäß der Datenschutzerklärung zu. *</span></div>
      <a class="btn">Nachricht senden</a>
    </form>
  </div>
</section>

<footer class="footer">
  <div class="container">
    <div class="cols">
      <div>
        <div class="brand"><i></i>pcwerk-rhein.de</div>
        <p>Seit 1997 Ihr vertrauensvoller Partner für professionelle IT-Dienstleistungen in Mainz.</p>
        <div class="social" aria-label="Soziale Netzwerke"><i></i><i></i><i></i></div>
      </div>
      <div>
        <h4>Kontakt</h4>
        <div class="fi"><svg class="ic"><use href="#i-pin"/></svg><span>Lindenweg 14<br>55116 Mainz, Deutschland</span></div>
        <div class="fi"><svg class="ic"><use href="#i-phone"/></svg><span>+49 6131 554870</span></div>
        <div class="fi"><svg class="ic"><use href="#i-mail"/></svg><span>info@pcwerk-rhein.de</span></div>
      </div>
      <div>
        <h4>Wichtige Links</h4>
        <ul><li>Home</li><li>Services</li><li>Kontakt</li><li>Impressum</li><li>Datenschutz</li></ul>
      </div>
    </div>
    <div class="copy">© 2025 brandt-it.eu - IT-Dienstleistungen Brandt. Alle Rechte vorbehalten.</div>
  </div>
</footer>
</body>
</html>
```